Word Template Designs for Offensive Security Professional Services Report

We need a Microsoft Word Template designed for our Offensive Security professional services reports which includes the following services:

RedTeaming
Network Penetration Testing
Web Application Penetration Testing
Wireless Penetration Testing
Social Engineering

The templates should include the following:
Cover Page design with our Logo included
Executive Summary Page design
Detailed Findings Page design
Design for Last Page

Lastly, I would also like a template I can use for all of my Statements of Work

Requirements
Must have
• Beautiful Eye Catching HD pictures that represent my Offensive Security projects
The design should flow well with our logo

```html
<!DOCTYPE html>
<html lang="en">
<head>
<meta charset="utf-8">
<title>Breachpoint – Scope of Work Template</title>
<link href="https://fonts.googleapis.com/css2?family=Lato:wght@400;700;900&display=swap" rel="stylesheet">
<style>
:root{
  --stage:#5b5b5b;
  --paper:#ffffff;
  --ink:#2b2b2b;
  --muted:#6d6d6d;
  --rule:#d9d9d9;
  --green:#7ab648;
  --green-dark:#4e8a2a;
  --circuit-deep:#1f3a22;
  --circuit-mid:#5f9a45;
  --circuit-light:#dfeed6;
}
*{box-sizing:border-box;margin:0;padding:0}
html,body{width:1200px;height:3596px;overflow:hidden}
body{background:var(--stage);font-family:'Lato',Arial,sans-serif;color:var(--ink);position:relative}
.page{position:absolute;width:440px;height:562px;background:var(--paper);padding:30px 30px 26px;overflow:hidden;font-size:5.4px;line-height:1.55}
.col-l{left:140px}.col-r{left:620px}.col-c{left:380px}
.r1{top:36px}.r2{top:634px}.r3{top:1232px}.r4{top:1830px}.r5{top:2428px}.r6{top:3026px}

.brand{display:flex;align-items:center;gap:5px;font-weight:900;font-size:9px;color:var(--ink)}
.brand .dot{width:16px;height:16px;border-radius:50%;background:var(--green)}
.brand-stack{flex-direction:column;gap:4px;font-size:10px}
.brand-stack .dot{width:26px;height:26px}

.page-title{font-weight:900;font-size:19px;letter-spacing:.3px;text-transform:uppercase;margin-bottom:10px;line-height:1.1}
.page-title .accent{color:var(--green)}
.section-head{font-weight:900;font-size:7px;text-transform:uppercase;margin:8px 0 4px;color:var(--ink)}
.section-head .accent{color:var(--green)}
p{margin-bottom:4px;color:#444}
ul.bullets{list-style:none;margin:2px 0 5px}
ul.bullets li{padding-left:7px;position:relative;margin-bottom:1.5px;color:#444}
ul.bullets li::before{content:"";position:absolute;left:1px;top:2.6px;width:2.4px;height:2.4px;border-radius:50%;background:var(--green)}
ol.tasks{margin:2px 0 4px 10px;color:#444}
ol.tasks li{margin-bottom:1.5px}
ol.tasks ul{margin-left:10px;list-style:circle}
.two-col{display:grid;grid-template-columns:1fr 1fr;column-gap:14px}
.ticks{list-style:none;display:grid;grid-template-columns:1fr 1fr;gap:3px 14px;margin:4px 0 6px}
.ticks li{display:flex;align-items:center;gap:4px;color:#444}
.ticks svg{width:6px;height:6px;flex:none}

.page-foot{position:absolute;left:30px;right:30px;bottom:14px;display:flex;justify-content:space-between;font-size:4.6px;color:var(--muted);border-top:.5px solid var(--rule);padding-top:4px}
.page-foot .web{color:var(--green-dark);font-weight:700}

/* cover */
.cover{padding:26px}
.cover .title{margin-top:78px;font-weight:900;font-size:11px;line-height:1.25;width:190px}
.cover .title .lead{display:block;text-transform:uppercase;font-size:10px;margin-bottom:2px}
.cover .prepared{margin-top:14px;font-weight:900;font-size:7px;text-transform:uppercase;color:var(--green-dark)}
.cover .prepared span{display:block;color:var(--ink);font-weight:700;text-transform:none}
.cover .contact{margin-top:18px;font-size:5px;color:#444;width:120px}
.cover .contact strong{display:block;font-size:6px;text-transform:uppercase;margin-bottom:2px}
.cover-visual{position:absolute;right:0;bottom:0;width:300px;height:380px;
  background:radial-gradient(circle at 55% 45%,var(--circuit-mid) 0%,var(--circuit-deep) 55%,rgba(31,58,34,0) 80%),linear-gradient(200deg,rgba(223,238,214,0) 10%,var(--circuit-light) 100%)}

/* revision table */
.rev-table{width:100%;border-collapse:collapse;font-size:5.4px;margin-top:6px}
.rev-table th{background:var(--green);color:#fff;font-weight:700;padding:4px 6px;text-align:left}
.rev-table td{padding:4px 6px;border-bottom:.5px solid var(--rule)}

/* toc */
.toc{list-style:none;margin-top:10px}
.toc li{display:flex;justify-content:space-between;padding:5px 0;border-bottom:.5px solid var(--rule);font-weight:700;font-size:5.2px}
.toc li.sub{font-weight:400;padding-left:8px;color:#555}

.sign{display:flex;gap:30px;margin-top:10px}
.sign div{flex:1;border-top:.5px solid #888;padding-top:2px;color:var(--muted)}

/* last page */
.back{display:flex;flex-direction:column;align-items:center;padding-top:70px;text-align:center}
.back .lines{margin-top:18px;font-size:5.2px;color:#444;line-height:2.2}
.back-visual{position:absolute;left:0;right:0;bottom:0;height:300px;
  background:linear-gradient(180deg,rgba(255,255,255,0) 0%,var(--circuit-light) 35%,var(--circuit-mid) 100%)}
</style>
</head>
<body>

<!-- Cover -->
<section class="page cover col-l r1">
  <div class="brand"><span class="dot"></span>Breachpoint</div>
  <h1 class="title"><span class="lead">Scope of Work :</span>External, Internal Network, Wireless and Web Application Penetration Testing Engagement</h1>
  <div class="prepared">Prepared For:<span>[Client Name]</span></div>
  <div class="contact">
    <strong>Prepared By:</strong>
    [Consultant Name]<br>Breachpoint Security<br>Office: (000) 000-0000<br>Mobile: (000) 000-0000<br>[Email Address]<br><br>
    Date: [Issue Date]<br>Version: 1.0
  </div>
  <div class="cover-visual" role="img" aria-label="Green glowing circuit board with security shield"></div>
</section>

<!-- Scope approval -->
<section class="page col-r r1">
  <h2 class="page-title"><span class="accent">Scope</span> Approval</h2>
  <h3 class="section-head">Client Activity <span class="accent">Checklist</span></h3>
  <ul class="bullets">
    <li>Provide a signed authorisation letter before testing begins.</li>
    <li>Confirm the external IP ranges and domains that are in scope.</li>
    <li>Supply internal network ranges and any excluded critical hosts.</li>
    <li>Name a technical contact available during all testing windows.</li>
    <li>Grant on-site or VPN access for the internal assessment phase.</li>
    <li>Share wireless SSIDs and office locations to be assessed.</li>
    <li>Provide test accounts for each web application user role.</li>
      <li>Notify hosting and cloud providers of planned test activity.</li>
    <li>Agree on emergency stop procedures and escalation contacts.</li>
    <li>Confirm maintenance windows and any blackout dates.</li>
  </ul>
  <p>The client agrees that the items above are completed prior to the engagement start date. Delays in these items may move the schedule and the final report delivery date.</p>
  <h3 class="section-head"><span class="accent">Acknowledgement</span></h3>
  <p>By signing below, the client confirms that the scope, targets and testing windows described in this document are accurate, and that Breachpoint is authorised to perform the activities listed for the systems named herein.</p>
  <p>Any change to the scope after signature must be agreed in writing by both parties and may affect the effort, cost and timeline of the engagement.</p>
  <p>Testing will only take place against assets owned or controlled by the client, unless written consent from a third party is supplied.</p>
  <p>Please sign and return this page to your Breachpoint consultant.</p>
  <div class="sign"><div>Client Signature</div><div>Date</div></div>
  <div class="sign"><div>Printed Name</div><div>Title</div></div>
  <footer class="page-foot"><span>Page 2</span><span class="web">www.breachpoint.example</span></footer>
</section>

<!-- Revision control -->
<section class="page col-l r2">
  <h2 class="page-title">Document Revision <span class="accent">Control</span></h2>
  <table class="rev-table">
    <thead><tr><th>Revision Number</th><th>Date</th><th>Revision Notes</th></tr></thead>
    <tbody><tr><td>1.0</td><td>[Date]</td><td>Initial release</td></tr></tbody>
  </table>
  <footer class="page-foot"><span>Page 3</span><span class="web">www.breachpoint.example</span></footer>
</section>

<!-- Table of contents -->
<section class="page col-r r2">
  <h2 class="page-title">Table of <span class="accent">Contents</span></h2>
  <ul class="toc">
    <li><span>Scope Approval</span><span>2</span></li>
    <li><span>Proposal Summary</span><span>5</span></li>
    <li class="sub"><span>Engagement Overview</span><span>5</span></li>
    <li class="sub"><span>Phase One: External Network Penetration Testing</span><span>5</span></li>
    <li class="sub"><span>Phase Two: Internal Network Penetration Testing</span><span>5</span></li>
    <li class="sub"><span>Phase Three: Wireless Penetration Testing</span><span>6</span></li>
    <li class="sub"><span>Phase Four: Web Application Penetration Testing</span><span>6</span></li>
    <li><span>Engagement Deliverables</span><span>6</span></li>
    <li><span>Phase Specific Tasks</span><span>7</span></li>
    <li class="sub"><span>Phase One: External Network Penetration Testing</span><span>7</span></li>
    <li class="sub"><span>Phase Two: Internal Network Penetration Testing</span><span>7</span></li>
    <li class="sub"><span>Phase Three: Wireless Penetration Testing</span><span>9</span></li>
    <li class="sub"><span>Phase Four: Web Application Penetration Testing</span><span>9</span></li>
    <li><span>Client Obligations</span><span>8</span></li>
    <li><span>Meeting Schedules</span><span>8</span></li>
    <li><span>Project Contacts</span><span>10</span></li>
  </ul>
  <footer class="page-foot"><span>Page 4</span><span class="web">www.breachpoint.example</span></footer>
</section>

<!-- Proposal summary -->
<section class="page col-l r3">
  <h2 class="page-title"><span class="accent">Proposal</span> Summary</h2>
  <p>Breachpoint has been asked to assess the security of the client's external and internal networks, wireless environment and key web applications. This document describes the activities, deliverables and responsibilities agreed for the engagement.</p>
  <h3 class="section-head">Engagement <span class="accent">Overview</span></h3>
  <p>The engagement is split into four phases. Each phase is run by a certified consultant and follows an industry recognised testing method, with findings rated by risk and paired with practical remediation advice.</p>
  <div class="two-col">
    <ul class="bullets"><li>External Network Penetration Testing</li><li>Internal Network Penetration Testing</li></ul>
    <ul class="bullets"><li>Wireless Penetration Testing</li><li>Web Application Penetration Testing</li></ul>
  </div>
  <h3 class="section-head">Phase One: <span class="accent">External Network Penetration Testing</span></h3>
  <p>This phase simulates an attacker on the internet with no prior knowledge of the environment. Consultants map exposed services, identify weaknesses in perimeter hosts and attempt controlled exploitation to show real business impact.</p>
  <p>Activities include host discovery, service enumeration, vulnerability scanning, manual validation of results and targeted exploitation of confirmed issues within the agreed rules of engagement.</p>
  <h3 class="section-head">Phase Two: <span class="accent">Internal Network Penetration Testing</span></h3>
  <p>This phase assumes an attacker has gained a foothold inside the network, such as a compromised workstation or a malicious insider. Consultants attempt to escalate privileges, move laterally and reach sensitive systems and data.</p>
  <p>The assessment reviews directory services, network segmentation, patch levels, credential hygiene and the detection capability of existing monitoring tools.</p>
  <footer class="page-foot"><span>Page 5</span><span class="web">www.breachpoint.example</span></footer>
</section>

<!-- Phase three / four -->
<section class="page col-r r3">
  <h3 class="section-head">Phase Three: <span class="accent">Wireless Penetration Testing</span></h3>
  <p>Consultants assess wireless networks at the agreed locations, reviewing encryption, authentication and guest isolation. Rogue access points and signal leakage beyond the premises are also identified and reported.</p>
  <h3 class="section-head">Phase Four: <span class="accent">Web Application Penetration Testing</span></h3>
  <p>Each in-scope application is tested by hand and with supporting tools, using authenticated and unauthenticated sessions. Testing follows a recognised web security standard and covers the following areas:</p>
  <ul class="ticks">
    <li><svg viewBox="0 0 10 10"><path d="M1 5.5l3 3 5-7" fill="none" stroke="#7ab648" stroke-width="2"/></svg>Information gathering</li>
    <li><svg viewBox="0 0 10 10"><path d="M1 5.5l3 3 5-7" fill="none" stroke="#7ab648" stroke-width="2"/></svg>Input validation</li>
    <li><svg viewBox="0 0 10 10"><path d="M1 5.5l3 3 5-7" fill="none" stroke="#7ab648" stroke-width="2"/></svg>Configuration management</li>
    <li><svg viewBox="0 0 10 10"><path d="M1 5.5l3 3 5-7" fill="none" stroke="#7ab648" stroke-width="2"/></svg>Error handling</li>
    <li><svg viewBox="0 0 10 10"><path d="M1 5.5l3 3 5-7" fill="none" stroke="#7ab648" stroke-width="2"/></svg>Identity management</li>
    <li><svg viewBox="0 0 10 10"><path d="M1 5.5l3 3 5-7" fill="none" stroke="#7ab648" stroke-width="2"/></svg>Weak cryptography</li>
    <li><svg viewBox="0 0 10 10"><path d="M1 5.5l3 3 5-7" fill="none" stroke="#7ab648" stroke-width="2"/></svg>Authentication</li>
    <li><svg viewBox="0 0 10 10"><path d="M1 5.5l3 3 5-7" fill="none" stroke="#7ab648" stroke-width="2"/></svg>Business logic</li>
    <li><svg viewBox="0 0 10 10"><path d="M1 5.5l3 3 5-7" fill="none" stroke="#7ab648" stroke-width="2"/></svg>Authorisation</li>
    <li><svg viewBox="0 0 10 10"><path d="M1 5.5l3 3 5-7" fill="none" stroke="#7ab648" stroke-width="2"/></svg>Client side testing</li>
    <li><svg viewBox="0 0 10 10"><path d="M1 5.5l3 3 5-7" fill="none" stroke="#7ab648" stroke-width="2"/></svg>Session management</li>
    <li><svg viewBox="0 0 10 10"><path d="M1 5.5l3 3 5-7" fill="none" stroke="#7ab648" stroke-width="2"/></svg>API security</li>
  </ul>
  <p>Findings from every phase are validated manually to remove false positives before they are included in the final report.</p>
  <h3 class="section-head">Engagement <span class="accent">Deliverables</span></h3>
  <ul class="bullets">
    <li>Executive summary for leadership</li>
    <li>Detailed technical findings with risk ratings and evidence</li>
    <li>Prioritised remediation roadmap for each phase</li>
    <li>Closing presentation and one round of retesting</li>
  </ul>
  <footer class="page-foot"><span>Page 6</span><span class="web">www.breachpoint.example</span></footer>
</section>

<!-- Phase specific tasks 1 -->
<section class="page col-l r4">
  <h2 class="page-title"><span class="accent">Phase Specific</span> Tasks</h2>
  <p>The following tasks will be completed during each phase of the engagement.</p>
  <h3 class="section-head">Phase One: <span class="accent">External Network Penetration Testing</span></h3>
  <ol class="tasks">
    <li>Reconnaissance
      <ul><li>Passive discovery of domains, hosts and exposed services</li><li>Review of public code, leaks and staff information</li></ul></li>
    <li>Scanning and enumeration
      <ul><li>Port and service scans of all in-scope addresses</li><li>Version detection and banner analysis</li></ul></li>
    <li>Vulnerability analysis
      <ul><li>Automated scanning with manual verification</li><li>Review of TLS, mail and remote access services</li></ul></li>
    <li>Exploitation of confirmed weaknesses within agreed limits</li>
    <li>Reporting of findings with evidence and advice</li>
  </ol>
  <h3 class="section-head">Phase Two: <span class="accent">Internal Network Penetration Testing</span></h3>
  <ol class="tasks">
    <li>Network discovery and host enumeration
      <ul><li>Identify live hosts, shares and key servers</li><li>Map trust relationships across segments</li></ul></li>
    <li>Directory service assessment
      <ul><li>Review of group policy, delegation and privileged accounts</li><li>Password policy and credential exposure checks</li></ul></li>
    <li>Privilege escalation and lateral movement
      <ul><li>Local misconfiguration and missing patch abuse</li><li>Credential reuse across systems</li></ul></li>
    <li>Segmentation testing between sensitive zones</li>
    <li>Data access review for critical business systems</li>
  </ol>
  <footer class="page-foot"><span>Page 7</span><span class="web">www.breachpoint.example</span></footer>
</section>

<!-- Client obligations 1 -->
<section class="page col-r r4">
  <h3 class="section-head">Client <span class="accent">Obligations</span></h3>
  <p>The client will provide timely access to systems, staff and information needed for the engagement, and will ensure that backups of critical systems are current before testing begins. Any outage or unexpected behaviour should be reported to the consultant at once.</p>
  <h3 class="section-head">Meeting <span class="accent">Schedules</span></h3>
  <ul class="bullets">
    <li>Kick-off meeting to confirm scope, contacts and timelines</li>
    <li>Closing meeting to present results and answer questions</li>
  </ul>
  <footer class="page-foot"><span>Page 8</span><span class="web">www.breachpoint.example</span></footer>
</section>

<!-- Phase specific tasks 2 -->
<section class="page col-l r5">
  <h3 class="section-head">Phase Three: <span class="accent">Wireless Penetration Testing</span></h3>
  <ol class="tasks">
    <li>Wireless survey
      <ul><li>Identify SSIDs, channels and signal coverage</li><li>Locate rogue and unauthorised access points</li></ul></li>
    <li>Encryption and authentication review
      <ul><li>Capture and analyse handshakes</li><li>Test enterprise authentication settings</li></ul></li>
    <li>Guest network isolation testing
      <ul><li>Attempt access to corporate resources</li><li>Review client isolation controls</li></ul></li>
    <li>Reporting of wireless findings</li>
  </ol>
  <h3 class="section-head">Phase Four: <span class="accent">Web Application Penetration Testing</span></h3>
  <ol class="tasks">
    <li>Application mapping
      <ul><li>Crawl content and identify entry points</li><li>Review roles, workflows and integrations</li></ul></li>
    <li>Authentication and session testing
      <ul><li>Login, reset and lockout controls</li><li>Token strength and session expiry</li></ul></li>
    <li>Input handling
      <ul><li>Injection, scripting and file upload checks</li><li>Server side request and deserialisation tests</li></ul></li>
    <li>Access control
      <ul><li>Horizontal and vertical privilege checks</li><li>Direct object reference testing</li></ul></li>
    <li>Business logic abuse and workflow bypass</li>
    <li>API endpoint review and rate limiting checks</li>
    <li>Reporting of application findings
      <ul><li>Risk rating and proof of concept</li><li>Clear steps to fix each issue</li></ul></li>
  </ol>
  <footer class="page-foot"><span>Page 9</span><span class="web">www.breachpoint.example</span></footer>
</section>

<!-- Client obligations 2 -->
<section class="page col-r r5">
  <h3 class="section-head">Client <span class="accent">Obligations</span></h3>
  <p>The client will name a point of contact for each phase, confirm change freeze periods and make sure relevant teams are aware of testing so that alerts are handled correctly. Access credentials must be issued before the phase they relate to.</p>
  <h3 class="section-head">Meeting <span class="accent">Schedules</span></h3>
  <ul class="bullets">
    <li>Weekly status call during active testing phases</li>
    <li>Report walkthrough within five days of delivery</li>
  </ul>
  <footer class="page-foot"><span>Page 10</span><span class="web">www.breachpoint.example</span></footer>
</section>

<!-- Back page -->
<section class="page back col-c r6">
  <div class="brand brand-stack"><span class="dot"></span>Breachpoint</div>
  <div class="lines">
    (000) 000-0000<br>
    [Email Address]<br>
    www.breachpoint.example
  </div>
  <div class="back-visual" role="img" aria-label="Soft green circuit board pattern fading upward"></div>
</section>

</body>
</html>
```